Plant Grower/Nursery needs a fun, professional and fresh 1/2 page print ad for a high profile gar...

We need a print ad for a garden tour geared towards plant enthusiasts that support California Native, natural and sustainable plants. A good percentage of our target market want a conservation and earth friendly approach to gardens/landscaping. We want to target this market, as well as, people who are looking for a pretty/colorful landscape that require little water/maintenance. **PLEASE LET US KNOW IF YOU HAVE QUESTIONS OR NEED MORE INFORMATION. WE ALSO HAVE MANY MORE PICTURES IF THESE DON'T WORK FOR YOUR DESIGN. ***THE AD CAN HAVE AS FEW AS 1 PHOTO - WE ARE POSTING SEVERAL IN HOPES THAT YOU CAN FIND WHAT IS PERFECT FOR YOUR IDEA!!Thank you

Target Market(s)

Gardeners, Landscapers, Landscape Designers/Architects, Cities and Municipalities.

Industry/Entity Type

Agriculture

Font styles to use
Serif
Sans Serif

Colors

Designer to choose colors to be used in the design.

Requirements
Must have
• We believe in growing regionally appropriate plants for Southern California that beatify our natural and urban landscapes.
• For over 20 years, our owners and staff take pride in providing timely, expert, and honest service.
Nice to have
• At least 1 photo. Eye catchy with a modern earthy feel.
• Hundreds of species/hybrids in stock of California Natives, Succulents, Ornamental Grasses, Standard Stock Items and Unique Plants.

```html
<!DOCTYPE html>
<html lang="en">
<head>
<meta charset="utf-8">
<title>Sol Verde Nursery – We believe! print ad</title>
<link rel="stylesheet" href="https://fonts.googleapis.com/css2?family=Questrial&family=Roboto:wght@300;400;700&display=swap">
<style>
  :root {
    --page: #e9eaec;
    --ad-bg: #e3e7ed;
    --ad-glow: #ffffff;
    --ink: #2a2a2c;
    --ink-soft: #4a4c50;
    --ink-light: #66686d;
    --rule: #8b8d92;
    --can: #b4b6b8;
    --petal: #b8479f;
    --ocean: #1f3257;
  }
  * { margin: 0; padding: 0; box-sizing: border-box; }
  html, body { width: 1200px; height: 1200px; overflow: hidden; }
  body {
    background: var(--page);
    position: relative;
    font-family: "Roboto", Arial, sans-serif;
  }
  .ad {
    position: absolute;
    left: 40px; top: 238px;
    width: 1120px; height: 723px;
    overflow: hidden;
    background:
      radial-gradient(circle at 260px 360px, var(--ad-glow) 0, rgba(255,255,255,0.75) 170px, rgba(255,255,255,0) 420px),
      var(--ad-bg);
  }
  .art-scene {
    position: absolute; left: 0; top: 0;
    width: 580px; height: 723px;
    background: linear-gradient(180deg,
      var(--can) 0%, #d3d5d8 18%, #eef0f3 28%,
      #d9b4de 40%, var(--petal) 58%, #cfc3d6 68%,
      #5d7560 76%, var(--ocean) 100%);
    -webkit-mask-image: linear-gradient(90deg, #000 0%, #000 62%, transparent 100%);
    mask-image: linear-gradient(90deg, #000 0%, #000 62%, transparent 100%);
  }
  .copy { position: absolute; right: 74px; text-align: right; white-space: nowrap; }
  .headline {
    top: 56px;
    font-family: "Questrial", "Century Gothic", sans-serif;
    font-weight: 400;
    font-size: 125px;
    line-height: 1;
    letter-spacing: -2px;
    color: var(--ink);
  }
  .lead {
    top: 167px;
    font-size: 25px;
    line-height: 31px;
    color: var(--ink-soft);
  }
  .rule {
    position: absolute; right: 74px; top: 280px;
    width: 118px; height: 3px;
    background: var(--rule);
  }
  .body-text {
    font-size: 17.5px;
    font-weight: 300;
    line-height: 22px;
    color: var(--ink-light);
  }
  .body-text.service { top: 291px; }
  .body-text.stock { top: 350px; }
  .contact-title {
    top: 425px;
    font-size: 18px; font-weight: 700; line-height: 22px;
    color: var(--ink);
  }
  .contact-line {
    display: flex; justify-content: flex-end; align-items: center; gap: 5px;
    font-size: 17.5px; line-height: 26px;
    color: var(--ink);
  }
  .contact-line.email { top: 447px; }
  .contact-line.phone { top: 473px; }
  .contact-line svg { width: 17px; height: 17px; }
  .brand {
    position: absolute; left: 820px; top: 542px;
    width: 236px;
    text-align: center;
  }
  .brand-mark {
    width: 73px; height: 73px;
    border: 2px solid var(--ink);
    margin: 0 auto 10px;
  }
  .brand-name {
    font-size: 20px; font-weight: 400;
    letter-spacing: 2px;
    line-height: 24px;
    color: var(--ink);
    border-bottom: 2px solid var(--ink);
    padding-bottom: 2px;
  }
  .brand-parent {
    font-size: 10px;
    color: var(--ink);
    margin-top: 5px;
    letter-spacing: 0.5px;
  }
</style>
</head>
<body>
  <section class="ad">
    <div class="art-scene" role="img" aria-label="Photo scene: a grey watering can at top left pours a purple and white flower down onto planet Earth seen from space"></div>

    <h1 class="copy headline">We believe!</h1>
    <p class="copy lead">We believe in growing regionally appropriate<br>plants for Southern California that beatify<br>our natural and urban landscapes.</p>
    <div class="rule"></div>
    <p class="copy body-text service">For over 20 years, our owners and staff take pride in<br>providing timely, expert, and honest service.</p>
    <p class="copy body-text stock">Hundreds of species/hybrids in stock of California<br>Natives, Succulents, Ornamental Grasses,<br>Standard Stock Items and Unique Plants.</p>
    <p class="copy contact-title">CONTACT US:</p>
    <p class="copy contact-line email">
      <svg viewBox="0 0 20 20" aria-hidden="true"><circle cx="10" cy="10" r="10" fill="#2a2a2c"/><rect x="5" y="6.5" width="10" height="7" fill="#fff"/><path d="M5 6.5 L10 10.5 L15 6.5" stroke="#2a2a2c" stroke-width="1.2" fill="none"/></svg>
      sales@solverdenursery.com
    </p>
    <p class="copy contact-line phone">
      <svg viewBox="0 0 20 20" aria-hidden="true"><circle cx="10" cy="10" r="10" fill="#2a2a2c"/><path d="M7 5 L9 7.5 L8 9 Q9 11 11 12 L12.5 11 L15 13 L13.5 15 Q9 15 6 11 Q5 8 7 5Z" fill="#fff"/></svg>
      555.014.2290
    </p>

    <div class="brand">
      <div class="brand-mark"></div>
      <p class="brand-name">SOL VERDE NURSERY</p>
      <p class="brand-parent">A Canyon Oak Holdings, Inc. Company</p>
    </div>
  </section>
</body>
</html>
```